Letterhead for Midwest Law Firm

Our law firm does estate planning and trust administration in Wisconsin and Illinois. We recently obtained a new logo and need to incorporate it into new stationary. The stationary needs to list out the attorneys at the firm, but we will want 3 variations, one with three attorneys, one with six, and one with six plus the names of states where each is licensed to practice (possibly as an asterisk with notation somewhere towards bottom of page. As with most traditional law practices, letterhead should be conservative and convey predictability and reliability. We view our brand as being primarily reliability, with prestige as a secondary element. We are upmarket, but would like to avoid seeming pretentious or "slick". We are a smaller firm with a personal touch.

Target Market(s)

Affluent Midwestern Americans approaching at or approaching retirement age.

Industry/Entity Type

Legal

Font styles to use
Serif
Sans Serif

Requirements
Must have
• Must use our logo. Must comply with Brennick Legal Guild Ethics rules: https://www.halvorjudic.org/courts/offices/docs/pqmtnv20annotated.pdf. Must be conventional. Must list names of attorneys and provide contact information for firm. Note that we are asking for three designs with very minor variations. Also, designer must provide letterhead in a format that is industry-standard for stationary printers.
Nice to have
• We would appreciate an alternate version that will look reasonable when printed on a black-and-white printer. Designer can use judgment as to whether to have use grayscale, black/white, or something in between.
Should not have
• No "motto" or "visit our website" extraneous materials. putting the website address somewhere is fine, but overall there is a lot of required text, and we'd like to not appear cluttered.

```html
<!DOCTYPE html>
<html lang="en">
<head>
<meta charset="utf-8">
<title>Hollister &amp; Vane LLP — Letterhead Set</title>
<link href="https://fonts.googleapis.com/css2?family=Lato:wght@400;700&display=swap" rel="stylesheet">
<style>
:root{
  --backdrop:#dcdde2;
  --paper:#ffffff;
  --navy:#2b2a3f;
  --blue:#0ba5df;
  --orange:#f2a11f;
  --ink:#2c2c34;
  --sign:#e4e5ea;
  --rule:#cfd0d6;
}
*{box-sizing:border-box;margin:0;padding:0}
html,body{width:1200px;height:2665px;overflow:hidden;background:var(--backdrop)}
body{position:relative;font-family:"Lato",Arial,sans-serif;color:var(--ink)}
.sheet{position:absolute;background:var(--paper);overflow:hidden}
.sheet--three{left:350px;top:95px;width:506px;height:717px}
.sheet--six{left:349px;top:980px;width:512px;height:724px}
.sheet--states{left:349px;top:1867px;width:512px;height:725px}

.firm{position:absolute;display:flex;align-items:center;gap:9px;color:var(--navy);font-family:"Lato",Arial,sans-serif;font-weight:700;font-size:17px;white-space:nowrap}
.firm__mark{width:14px;height:14px;background:var(--navy);flex:none}
.sheet--three .firm{left:42px;top:80px}
.sheet--six .firm,.sheet--states .firm{left:0;right:0;justify-content:center;top:40px}

.roster{position:absolute;font-size:8.6px;font-weight:700;text-transform:uppercase;color:var(--navy);line-height:17px;white-space:nowrap}
.roster .role{color:var(--orange);font-weight:400;text-transform:none}
.roster--right{text-align:right}
.sheet--three .roster{right:42px;top:40px}
.sheet--six .roster--left{left:42px;top:100px}
.sheet--six .roster--right{right:42px;top:100px}
.sheet--states .roster{top:97px;font-size:6.8px;line-height:17px}
.sheet--states .col1{left:43px}
.sheet--states .col2{left:190px;padding-left:14px;border-left:1px solid var(--rule)}
.sheet--states .col3{left:334px;padding-left:14px;border-left:1px solid var(--rule)}
.lic{color:var(--navy);font-weight:700}

.tab{position:absolute;width:28px;height:50px;background:var(--blue)}
.sheet--three .tab--right{right:0;top:38px;width:25px}
.sheet--six .tab,.sheet--states .tab{top:97px}
.tab--left{left:0}
.tab--right{right:0}

.letter{position:absolute;left:43px;right:43px;font-size:8.4px;line-height:11.2px}
.sheet--three .letter{top:137px}
.sheet--six .letter{top:183px}
.sheet--states .letter{top:177px}
.letter__meta{display:flex;justify-content:space-between;font-size:8.8px}
.letter__subject{text-align:center;font-size:12px;font-weight:700;text-decoration:underline;text-underline-offset:2px;color:var(--navy);margin:33px 0 49px}
.sheet--states .letter__subject{margin:26px 0 34px}
.letter__salute{font-size:8.8px;margin-bottom:6px}
.letter p{margin-bottom:6px;text-align:justify}
.closing{margin:38px 0 0 auto;width:130px;text-align:center;font-size:8.8px}
.sheet--states .closing{margin-top:30px}
.signature{display:block;width:118px;height:30px;margin:10px auto 8px;background:var(--sign);border-radius:3px}
.closing__name{font-weight:700;color:var(--navy)}

.licensing{position:absolute;left:43px;bottom:48px;font-size:7px;color:var(--navy);display:flex;gap:18px}

.footer{position:absolute;left:0;right:0;bottom:11px;height:29px;color:#fff;font-size:9.2px;line-height:11px}
.footer svg.band{position:absolute;inset:0;width:100%;height:100%}
.footer__addr{position:absolute;left:40px;top:3px;display:flex;gap:8px}
.footer__phone{position:absolute;left:362px;top:3px}
.footer__phone div{display:flex;align-items:center;gap:6px}
.ico{width:9px;height:9px;flex:none;margin-top:1px}
</style>
</head>
<body>

<section class="sheet sheet--three" aria-label="Letterhead, three names">
  <div class="firm"><span class="firm__mark"></span>Hollister &amp; Vane LLP</div>
  <div class="roster roster--right">
    <div>Gerald T. Hollister, <span class="role">Attorney</span></div>
    <div>Martin E. Hollister, <span class="role">Attorney</span></div>
    <div>Ruth A. Pellman, <span class="role">Paralegal</span></div>
  </div>
  <div class="tab tab--right"></div>
  <div class="letter">
    <div class="letter__meta"><span>Ref. No.</span><span>March 10, 2021</span></div>
    <h1 class="letter__subject">YOUR SUBJECT GOES HERE</h1>
    <div class="letter__salute">Dear X</div>
    <p>Lorem Ipsum is simply dummy text of the printing and typesetting industry. Lorem Ipsum has been the industry's standard dummy text ever since the 1500s, when an unknown printer took a galley of type and scrambled it to make a type specimen book. It has survived not only five centuries, but also the leap into electronic typesetting, remaining essentially unchanged. It was popularised in the 1960s with the release of Letraset sheets containing Lorem Ipsum passages, and more recently with desktop publishing software like Aldus PageMaker including versions of Lorem Ipsum.</p>
    <p>Lorem Ipsum is simply dummy text of the printing and typesetting industry. Lorem Ipsum has been the industry's standard dummy text ever since the 1500s, when an unknown printer took a galley of type and scrambled it to make a type specimen book. It has survived not only five centuries, but also the leap into electronic typesetting, remaining essentially unchanged.</p>
    <p>It was popularised in the 1960s with the release of Letraset sheets containing Lorem Ipsum passages, and more recently with desktop publishing software like Aldus PageMaker including versions of Lorem Ipsum.</p>
    <p>Lorem Ipsum is simply dummy text of the printing and typesetting industry. Lorem Ipsum has been the industry's standard dummy text ever since the 1500s, when an unknown printer took a galley of type and scrambled it to make a type specimen book. It has survived not only five centuries, but also the leap into electronic typesetting, remaining essentially unchanged. It was popularised in the 1960s with the release of Letraset sheets containing Lorem Ipsum passages, and more recently with desktop publishing software like Aldus PageMaker including versions of Lorem Ipsum.</p>
    <div class="closing">Very truly yours,<span class="signature" role="img" aria-label="Handwritten signature"></span><div class="closing__name">MARTIN E. HOLLISTER</div></div>
  </div>
  <footer class="footer">
    <svg class="band" viewBox="0 0 506 29" preserveAspectRatio="none"><polygon points="0,0 336,0 314,29 0,29" fill="var(--blue)"/><polygon points="344,0 506,0 506,29 322,29" fill="var(--navy)"/></svg>
    <div class="footer__addr"><svg class="ico" viewBox="0 0 10 10"><path d="M5 .8a3.3 3.3 0 0 0-3.3 3.3C1.7 6.6 5 9.4 5 9.4s3.3-2.8 3.3-5.3A3.3 3.3 0 0 0 5 .8z" fill="none" stroke="#fff" stroke-width="1"/><circle cx="5" cy="4.1" r="1.1" fill="#fff"/></svg><span>218 West Larchmont Avenue, Suite<br>300&nbsp; Milwaukee, Wisconsin 53210</span></div>
    <div class="footer__phone">
      <div><svg class="ico" viewBox="0 0 10 10"><path d="M2.2 1l1.6 1.9-.8 1.2a6 6 0 0 0 2.9 2.9l1.2-.8L9 7.8 8 9C4.3 8.8 1.2 5.7 1 2z" fill="none" stroke="#fff" stroke-width=".9"/></svg>414-555-0182</div>
      <div><svg class="ico" viewBox="0 0 10 10"><rect x="2.5" y="1" width="5" height="3" fill="none" stroke="#fff" stroke-width=".9"/><rect x="1" y="4" width="8" height="4" rx=".8" fill="none" stroke="#fff" stroke-width=".9"/><rect x="3" y="6.5" width="4" height="2.5" fill="#fff"/></svg>FAX 414-555-0147</div>
    </div>
  </footer>
</section>

<section class="sheet sheet--six" aria-label="Letterhead, six names">
  <div class="firm"><span class="firm__mark"></span>Hollister &amp; Vane LLP</div>
  <div class="tab tab--left"></div>
  <div class="tab tab--right"></div>
  <div class="roster roster--left">
    <div>Tobias L. Wrenfield, <span class="role">Sr. Associate</span></div>
    <div>Claire D. Ostrander, <span class="role">Sr. Associate</span></div>
    <div>Nora B. Kestelyn, <span class="role">Sr. Associate</span></div>
  </div>
  <div class="roster roster--right">
    <div>Gerald T. Hollister, <span class="role">Attorney</span></div>
    <div>Martin E. Hollister, <span class="role">Attorney</span></div>
    <div>Ruth A. Pellman, <span class="role">Paralegal</span></div>
  </div>
  <div class="letter">
    <div class="letter__meta"><span>Ref. No.</span><span>March 10, 2021</span></div>
    <h1 class="letter__subject">YOUR SUBJECT GOES HERE</h1>
    <div class="letter__salute">Dear X</div>
    <p>Lorem Ipsum is simply dummy text of the printing and typesetting industry. Lorem Ipsum has been the industry's standard dummy text ever since the 1500s, when an unknown printer took a galley of type and scrambled it to make a type specimen book. It has survived not only five centuries, but also the leap into electronic typesetting, remaining essentially unchanged. It was popularised in the 1960s with the release of Letraset sheets containing Lorem Ipsum passages, and more recently with desktop publishing software like Aldus PageMaker including versions of Lorem Ipsum.</p>
    <p>Lorem Ipsum is simply dummy text of the printing and typesetting industry. Lorem Ipsum has been the industry's standard dummy text ever since the 1500s, when an unknown printer took a galley of type and scrambled it to make a type specimen book. It has survived not only five centuries, but also the leap into electronic typesetting, remaining essentially unchanged.</p>
    <p>It was popularised in the 1960s with the release of Letraset sheets containing Lorem Ipsum passages, and more recently with desktop publishing software like Aldus PageMaker including versions of Lorem Ipsum.</p>
    <p>Lorem Ipsum is simply dummy text of the printing and typesetting industry. Lorem Ipsum has been the industry's standard dummy text ever since the 1500s, when an unknown printer took a galley of type and scrambled it to make a type specimen book. It has survived not only five centuries, but also the leap into electronic typesetting, remaining essentially unchanged. It was popularised in the 1960s with the release of Letraset sheets containing Lorem Ipsum passages, and more recently with desktop publishing software like Aldus PageMaker including versions of Lorem Ipsum.</p>
    <div class="closing">Very truly yours,<span class="signature" role="img" aria-label="Handwritten signature"></span><div class="closing__name">MARTIN E. HOLLISTER</div></div>
  </div>
  <footer class="footer">
    <svg class="band" viewBox="0 0 512 29" preserveAspectRatio="none"><polygon points="0,0 340,0 318,29 0,29" fill="var(--blue)"/><polygon points="348,0 512,0 512,29 326,29" fill="var(--navy)"/></svg>
    <div class="footer__addr"><svg class="ico" viewBox="0 0 10 10"><path d="M5 .8a3.3 3.3 0 0 0-3.3 3.3C1.7 6.6 5 9.4 5 9.4s3.3-2.8 3.3-5.3A3.3 3.3 0 0 0 5 .8z" fill="none" stroke="#fff" stroke-width="1"/><circle cx="5" cy="4.1" r="1.1" fill="#fff"/></svg><span>218 West Larchmont Avenue, Suite<br>300&nbsp; Milwaukee, Wisconsin 53210</span></div>
    <div class="footer__phone">
      <div><svg class="ico" viewBox="0 0 10 10"><path d="M2.2 1l1.6 1.9-.8 1.2a6 6 0 0 0 2.9 2.9l1.2-.8L9 7.8 8 9C4.3 8.8 1.2 5.7 1 2z" fill="none" stroke="#fff" stroke-width=".9"/></svg>414-555-0182</div>
      <div><svg class="ico" viewBox="0 0 10 10"><rect x="2.5" y="1" width="5" height="3" fill="none" stroke="#fff" stroke-width=".9"/><rect x="1" y="4" width="8" height="4" rx=".8" fill="none" stroke="#fff" stroke-width=".9"/><rect x="3" y="6.5" width="4" height="2.5" fill="#fff"/></svg>FAX 414-555-0147</div>
    </div>
  </footer>
</section>

<section class="sheet sheet--states" aria-label="Letterhead, names with state licensing">
  <div class="firm"><span class="firm__mark"></span>Hollister &amp; Vane LLP</div>
  <div class="tab tab--left"></div>
  <div class="tab tab--right"></div>
  <div class="roster col1">
    <div>Gerald T. Hollister<span class="lic">*</span>, <span class="role">Attorney</span></div>
    <div>Martin E. Hollister<span class="lic">**</span>, <span class="role">Attorney</span></div>
    <div>Ruth A. Pellman, <span class="role">Paralegal</span></div>
  </div>
  <div class="roster col2">
    <div>Gerald T. Hollister<span class="lic">*</span>, <span class="role">Attorney</span></div>
    <div>Martin E. Hollister<span class="lic">**</span>, <span class="role">Attorney</span></div>
    <div>Ruth A. Pellman, <span class="role">Paralegal</span></div>
  </div>
  <div class="roster col3">
    <div>Tobias L. Wrenfield<span class="lic">*</span>, <span class="role">Sr. Associate</span></div>
    <div>Claire D. Ostrander<span class="lic">**</span>, <span class="role">Sr. Associate</span></div>
    <div>Nora B. Kestelyn<span class="lic">*</span>, <span class="role">Sr. Associate</span></div>
  </div>
  <div class="letter">
    <div class="letter__meta"><span>Ref. No.</span><span>March 10, 2021</span></div>
    <h1 class="letter__subject">YOUR SUBJECT GOES HERE</h1>
    <div class="letter__salute">Dear X</div>
    <p>Lorem Ipsum is simply dummy text of the printing and typesetting industry. Lorem Ipsum has been the industry's standard dummy text ever since the 1500s, when an unknown printer took a galley of type and scrambled it to make a type specimen book. It has survived not only five centuries, but also the leap into electronic typesetting, remaining essentially unchanged. It was popularised in the 1960s with the release of Letraset sheets containing Lorem Ipsum passages, and more recently with desktop publishing software like Aldus PageMaker including versions of Lorem Ipsum.</p>
    <p>Lorem Ipsum is simply dummy text of the printing and typesetting industry. Lorem Ipsum has been the industry's standard dummy text ever since the 1500s, when an unknown printer took a galley of type and scrambled it to make a type specimen book. It has survived not only five centuries, but also the leap into electronic typesetting, remaining essentially unchanged.</p>
    <p>It was popularised in the 1960s with the release of Letraset sheets containing Lorem Ipsum passages, and more recently with desktop publishing software like Aldus PageMaker including versions of Lorem Ipsum.</p>
    <p>Lorem Ipsum is simply dummy text of the printing and typesetting industry. Lorem Ipsum has been the industry's standard dummy text ever since the 1500s, when an unknown printer took a galley of type and scrambled it to make a type specimen book. It has survived not only five centuries, but also the leap into electronic typesetting, remaining essentially unchanged. It was popularised in the 1960s with the release of Letraset sheets containing Lorem Ipsum passages, and more recently with desktop publishing software like Aldus PageMaker including versions of Lorem Ipsum.</p>
    <div class="closing">Very truly yours,<span class="signature" role="img" aria-label="Handwritten signature"></span><div class="closing__name">MARTIN E. HOLLISTER</div></div>
  </div>
  <div class="licensing"><span>* Licensed in Wisconsin</span><span>** Licensed in Wisconsin and Illinois</span></div>
  <footer class="footer">
    <svg class="band" viewBox="0 0 512 29" preserveAspectRatio="none"><polygon points="0,0 340,0 318,29 0,29" fill="var(--blue)"/><polygon points="348,0 512,0 512,29 326,29" fill="var(--navy)"/></svg>
    <div class="footer__addr"><svg class="ico" viewBox="0 0 10 10"><path d="M5 .8a3.3 3.3 0 0 0-3.3 3.3C1.7 6.6 5 9.4 5 9.4s3.3-2.8 3.3-5.3A3.3 3.3 0 0 0 5 .8z" fill="none" stroke="#fff" stroke-width="1"/><circle cx="5" cy="4.1" r="1.1" fill="#fff"/></svg><span>218 West Larchmont Avenue, Suite<br>300&nbsp; Milwaukee, Wisconsin 53210</span></div>
    <div class="footer__phone">
      <div><svg class="ico" viewBox="0 0 10 10"><path d="M2.2 1l1.6 1.9-.8 1.2a6 6 0 0 0 2.9 2.9l1.2-.8L9 7.8 8 9C4.3 8.8 1.2 5.7 1 2z" fill="none" stroke="#fff" stroke-width=".9"/></svg>414-555-0182</div>
      <div><svg class="ico" viewBox="0 0 10 10"><rect x="2.5" y="1" width="5" height="3" fill="none" stroke="#fff" stroke-width=".9"/><rect x="1" y="4" width="8" height="4" rx=".8" fill="none" stroke="#fff" stroke-width=".9"/><rect x="3" y="6.5" width="4" height="2.5" fill="#fff"/></svg>FAX 414-555-0147</div>
    </div>
  </footer>
</section>

</body>
</html>
```